WPF Application Design

I require a design for a WPF application. I have the screenshots which needs to be redesigned for WPF application. Screens have different standard controls used, designer should suggest best placement and styling for the screens.

```html
<!DOCTYPE html>
<html lang="en">
<head>
<meta charset="utf-8">
<title>Course Template</title>
<link href="https://fonts.googleapis.com/css2?family=Source+Sans+3:wght@300;400&display=swap" rel="stylesheet">
<style>
  :root {
    --page-bg: #ffffff;
    --brand-blue: #1f74bd;
    --text-dark: #3a3a3a;
    --text-muted: #c4c8cc;
    --band-grey: #e6e7e8;
    --field-border: #bfc3c7;
    --radio-border: #b9bcc0;
    --white: #ffffff;
  }
  * { box-sizing: border-box; margin: 0; padding: 0; }
  html, body { width: 1200px; height: 900px; overflow: hidden; background: var(--page-bg); }
  body { position: relative; font-family: "Source Sans 3", "Source Sans Pro", sans-serif; color: var(--text-dark); }

  .window {
    position: absolute; left: 90px; top: 84px; width: 1020px; height: 703px;
    background: var(--white);
    box-shadow: 0 2px 8px rgba(0,0,0,0.35);
  }
  .title-bar {
    position: absolute; left: 0; top: 0; width: 100%; height: 106px;
    background: var(--brand-blue);
  }
  .window-title {
    position: absolute; left: 0; right: 0; top: 32px; text-align: center;
    color: var(--white); font-weight: 300; font-size: 29px; letter-spacing: 0.2px;
  }
  .window-controls { position: absolute; right: 16px; top: 12px; }

  .tab-bar { position: absolute; left: 0; top: 106px; width: 100%; height: 85px; }
  .tab {
    position: absolute; top: 14px; width: 130px; height: 55px;
    display: flex; align-items: center; justify-content: center; text-align: center;
    font-size: 16.5px; line-height: 22px; color: var(--brand-blue);
  }
  .tab.is-disabled { color: var(--text-muted); }
  .tab.is-active { border: 1px solid var(--brand-blue); }
  .tab-band { position: absolute; left: 0; top: 191px; width: 100%; height: 7px; background: var(--band-grey); }
  .footer-band { position: absolute; left: 0; bottom: 0; width: 100%; height: 17px; background: var(--band-grey); }

  .field-group { position: absolute; width: 260px; height: 130px; }
  .group-label { position: absolute; left: 0; top: 0; font-size: 16.5px; }
  .option-row { position: absolute; left: 0; height: 26px; display: flex; align-items: center; font-size: 16.5px; }
  .option-row.first { top: 59px; }
  .option-row.second { top: 94px; }

  .radio {
    width: 27px; height: 27px; border-radius: 50%;
    border: 1px solid var(--radio-border); background: var(--white);
    margin-right: 24px; position: relative; flex: none;
  }
  .radio.is-checked::after {
    content: ""; position: absolute; left: 5px; top: 5px; width: 15px; height: 15px;
    border-radius: 50%; background: var(--brand-blue);
  }
  .number-input {
    width: 58px; height: 23px; border: 1px solid var(--field-border);
    display: flex; align-items: center; justify-content: center; font-size: 16px; flex: none;
  }
  .duration .number-input { margin-right: 12px; }
  .participants .number-input { margin-right: 5px; }
  .participants .option-row.second { top: 94px; }
  .participants .option-row.first { top: 59px; }
</style>
</head>
<body>
  <div class="window">
    <header class="title-bar">
      <h1 class="window-title">Course Template</h1>
      <svg class="window-controls" width="96" height="20" viewBox="0 0 96 20" aria-label="Window controls">
        <line x1="2" y1="10" x2="18" y2="10" stroke="#fff" stroke-width="2"/>
        <rect x="40" y="3" width="14" height="13" fill="none" stroke="#fff" stroke-width="2"/>
        <line x1="79" y1="3" x2="91" y2="15" stroke="#fff" stroke-width="2.2"/>
        <line x1="91" y1="3" x2="79" y2="15" stroke="#fff" stroke-width="2.2"/>
      </svg>
    </header>

    <nav class="tab-bar">
      <div class="tab is-active" style="left:7px;">Template<br>Type</div>
      <div class="tab" style="left:138px;">General</div>
      <div class="tab" style="left:269px;">Finance</div>
      <div class="tab is-disabled" style="left:400px;">Preliminary<br>Course</div>
      <div class="tab is-disabled" style="left:531px;">Package</div>
      <div class="tab" style="left:663px;">Learning<br>Goals</div>
      <div class="tab" style="left:795px;">Remark</div>
    </nav>
    <div class="tab-band"></div>

    <section class="field-group duration" style="left:81px; top:260px;">
      <div class="group-label">Club duration (unit)</div>
      <div class="option-row first"><span class="radio"></span><span class="number-input">0</span>Minutes</div>
      <div class="option-row second"><span class="radio is-checked"></span>Individuals</div>
    </section>
    <section class="field-group participants" style="left:438px; top:260px;">
      <div class="group-label">Number Of Participants</div>
      <div class="option-row first"><span class="number-input">0</span>Minimum</div>
      <div class="option-row second" style="top:94px;"><span class="number-input">0</span>Maximum</div>
    </section>
    <section class="field-group duration" style="left:748px; top:260px;">
      <div class="group-label">Club duration (unit)</div>
      <div class="option-row first"><span class="radio"></span><span class="number-input">0</span>Minutes</div>
      <div class="option-row second"><span class="radio is-checked"></span>Individuals</div>
    </section>

    <section class="field-group duration" style="left:81px; top:494px;">
      <div class="group-label">Club duration (unit)</div>
      <div class="option-row first"><span class="radio"></span><span class="number-input">0</span>Minutes</div>
      <div class="option-row second"><span class="radio is-checked"></span>Individuals</div>
    </section>
    <section class="field-group participants" style="left:438px; top:494px;">
      <div class="group-label">Number Of Participants</div>
      <div class="option-row first"><span class="number-input">0</span>Minimum</div>
      <div class="option-row second"><span class="number-input">0</span>Maximum</div>
    </section>
    <section class="field-group duration" style="left:748px; top:494px;">
      <div class="group-label">Club duration (unit)</div>
      <div class="option-row first"><span class="radio"></span><span class="number-input">0</span>Minutes</div>
      <div class="option-row second"><span class="radio is-checked"></span>Individuals</div>
    </section>

    <div class="footer-band"></div>
  </div>
</body>
</html>
```